Corin Abbott Business Cards

We Need two Business Cards with bleeds. the only difference between the two cards is the backaround color one lilac and pink. Attached we have the cards please match up the logo's and text. Take out the orange box out.

Target Market(s)

double-sided business cards

Industry/Entity Type

Business

Logo Text

match up as best as possible

Colors
f59195
d2a4cc

Requirements
Must have
• n/a
Nice to have
• n/a
Should not have
• n/a

```html
<!DOCTYPE html>
<html lang="en">
<head>
<meta charset="utf-8">
<title>Corin Abbott-Hale, MD – Business Card</title>
<link rel="stylesheet" href="https://fonts.googleapis.com/css2?family=Libre+Baskerville:wght@400;700&family=Dancing+Script:wght@700&display=swap">
<style>
  :root {
    --page: #ffffff;
    --card-lilac: #dcc0e0;
    --card-edge: #b9a9bb;
    --shadow: #b5b5b5;
    --ink: #1c1718;
    --accent: #8a474d;
  }
  * { margin: 0; padding: 0; box-sizing: border-box; }
  html, body { width: 1200px; height: 705px; overflow: hidden; background: var(--page); }
  .canvas { position: relative; width: 1200px; height: 705px; }
  .card {
    position: absolute; left: 15px; top: 14px; width: 1165px; height: 664px;
    background: var(--card-lilac);
    border: 1px solid var(--card-edge);
    box-shadow: 9px 9px 0 var(--shadow);
    font-family: "Libre Baskerville", Georgia, serif;
    color: var(--ink);
  }
  .card > * { position: absolute; line-height: 1; white-space: nowrap; }
  .doctor-name { left: 0; width: 100%; top: 66px; text-align: center; font-size: 56px; font-weight: 700; }
  .certification { left: 0; width: 100%; top: 137px; text-align: center; font-size: 33px; font-weight: 700; letter-spacing: 4px; }
  .specialty { left: 219px; top: 229px; color: var(--accent); font-size: 44px; }
  .specialty .script { font-family: "Dancing Script", cursive; font-weight: 700; font-size: 56px; letter-spacing: 6px; margin-right: 8px; }
  .specialty-rule { left: 214px; top: 281px; width: 879px; height: 2px; background: var(--accent); }
  .logo-mark { left: 73px; top: 232px; width: 152px; height: 223px; }
  .service { font-size: 35px; font-weight: 700; }
  .service-1 { left: 247px; top: 304px; }
  .service-2 { left: 244px; top: 341px; }
  .service-3 { left: 231px; top: 378px; }
  .service-4 { left: 217px; top: 414px; }
  .service-5 { left: 184px; top: 450px; }
  .appointment { left: 205px; top: 570px; font-size: 27px; }
  .contact { left: 645px; font-weight: 700; }
  .address-1 { top: 374px; font-size: 32px; }
  .address-2 { top: 423px; font-size: 31px; }
  .phone { top: 469px; font-size: 31px; letter-spacing: 9px; }
  .fax { top: 514px; font-size: 31px; letter-spacing: 9px; }
  .email { top: 564px; font-size: 28px; }
</style>
</head>
<body>
<div class="canvas">
  <section class="card">
    <h1 class="doctor-name">Corin Abbott -Hale , MD</h1>
    <p class="certification">Board Certified</p>

    <svg class="logo-mark" viewBox="0 0 152 223" role="img" aria-label="Practice logo mark: mother and child emblem">
      <rect x="0" y="0" width="152" height="223" rx="70" fill="#c9a3bf"/>
    </svg>

    <p class="specialty"><span class="script">Womens Helth</span>&amp; Wellness Specialist</p>
    <div class="specialty-rule"></div>

    <p class="service service-1">Obstetrics</p>
    <p class="service service-2">Gynecology</p>
    <p class="service service-3">Family Planning</p>
    <p class="service service-4">Weight Management</p>
    <p class="service service-5">Menopause</p>

    <p class="appointment">BY APPOINTMENT</p>

    <p class="contact address-1">248-15 Maplewood Parkway</p>
    <p class="contact address-2">Maplewood, New York 11590</p>
    <p class="contact phone">(PH) 718.555.0142</p>
    <p class="contact fax">(FX) 718.555.0143</p>
    <p class="contact email">(Email) c-hale@mailbox.net</p>
  </section>
</div>
</body>
</html>
```